Granite Ridge Holdings

I have a real estate investment business.

** I need editable vector files of the final design.

Industry/Entity Type

Real Estate

Contact Information for Business Card

I would like the card to be clear and direct with the company name and contact info. I would prefer not to have a design that is too busy (i.e., with excessive detail) in the business card.

Font styles to use
Sans Serif

Requirements
Must have
• My card must have the following information listed below:
• Company name: Grainite Ridge Holdings LLC
• My name: Daniel Vorsley
• Phone number: (555) 218-9067
• Email address: dtvorsley@mailbox-example.net
• Keywords: “Real Estate Investments”
Nice to have
• I would like to have a design that resembles the characteristics/uses of obsidian stone which resembles something related to strength and resilience. Perhaps something with sharp, sleek color transitions as well.

```html
<!DOCTYPE html>
<html lang="en">
<head>
<meta charset="utf-8">
<title>Granite Ridge Holdings – Business Card</title>
<link href="https://fonts.googleapis.com/css2?family=Poppins:wght@400;600&family=Arimo:wght@400&display=swap" rel="stylesheet">
<style>
  :root {
    --stage: #2b2b2d;
    --obsidian: #050505;
    --paper: #ffffff;
    --ink: #111111;
    --rule: #1a1a1a;
    --band-grey: #6a6a6a;
  }
  * { margin: 0; padding: 0; box-sizing: border-box; }
  html, body { width: 1200px; height: 1200px; overflow: hidden; background: var(--stage); }
  .canvas { position: relative; width: 1200px; height: 1200px; }

  .card { position: absolute; left: 160px; width: 880px; height: 500px; overflow: hidden; }

  /* Front */
  .card-front { top: 70px; background: var(--obsidian); color: var(--paper); }
  .front-wordmark {
    position: absolute; left: 280px; top: 170px;
    font-family: "Poppins", sans-serif; font-weight: 600; text-align: right;
  }
  .front-wordmark .line-main { font-size: 52px; line-height: 1.05; }
  .front-wordmark .line-sub { font-size: 36px; line-height: 1.05; }
  .front-tagline {
    position: absolute; left: 280px; top: 300px; width: 460px;
    font-family: "Poppins", sans-serif; font-weight: 400;
    font-size: 21px; letter-spacing: 6px; text-align: right;
  }

  /* Back */
  .card-back { top: 630px; background: var(--paper); color: var(--ink); }
  .brand { position: absolute; left: 60px; top: 50px; display: flex; align-items: flex-end; gap: 22px; }
  .brand-square { width: 104px; height: 104px; background: var(--obsidian); }
  .brand-name { font-family: "Poppins", sans-serif; font-weight: 600; color: var(--ink); text-align: right; }
  .brand-name .line-main { font-size: 46px; line-height: 1.05; }
  .brand-name .line-sub { font-size: 32px; line-height: 1.05; }

  .person {
    position: absolute; left: 60px; top: 232px; width: 250px;
    font-family: "Poppins", sans-serif; font-weight: 600; font-size: 22px;
    padding-bottom: 4px; border-bottom: 2px solid var(--rule);
  }
  .contact-list { position: absolute; left: 60px; top: 290px; list-style: none; font-family: "Arimo", sans-serif; font-size: 20px; }
  .contact-list li { display: flex; align-items: center; gap: 10px; height: 32px; }
  .contact-icon { width: 22px; height: 22px; border-radius: 50%; background: var(--ink); display: flex; align-items: center; justify-content: center; }
  .divider { position: absolute; left: 310px; right: 60px; top: 262px; height: 2px; background: var(--rule); }
  .base-band { position: absolute; left: 0; bottom: 0; width: 880px; height: 80px; }
</style>
</head>
<body>
<main class="canvas">

  <section class="card card-front" aria-label="Card front">
    <div class="front-wordmark">
      <div class="line-main">Grainite Ridge</div>
      <div class="line-sub">Holdings LLC</div>
    </div>
    <p class="front-tagline">Real Estate Investments</p>
  </section>

  <section class="card card-back" aria-label="Card back">
    <div class="brand">
      <span class="brand-square" aria-hidden="true"></span>
      <div class="brand-name">
        <div class="line-main">Grainite Ridge</div>
        <div class="line-sub">Holdings LLC</div>
      </div>
    </div>

    <p class="person">Daniel Vorsley</p>
    <span class="divider" aria-hidden="true"></span>

    <ul class="contact-list">
      <li>
        <span class="contact-icon" aria-hidden="true">
          <svg width="12" height="14" viewBox="0 0 12 14"><rect x="2" y="1" width="8" height="12" rx="1.5" fill="none" stroke="#fff" stroke-width="1.6"/></svg>
        </span>
        (555) 218-9067
      </li>
      <li>
        <span class="contact-icon" aria-hidden="true">
          <svg width="14" height="10" viewBox="0 0 14 10"><rect x="1" y="1" width="12" height="8" fill="none" stroke="#fff" stroke-width="1.4"/><path d="M1 1 L7 6 L13 1" fill="none" stroke="#fff" stroke-width="1.4"/></svg>
        </span>
        dtvorsley@mailbox-example.net
      </li>
    </ul>

    <svg class="base-band" viewBox="0 0 880 80" aria-hidden="true">
      <path d="M0 48 H640 L654 30 H880 V80 H0 Z" fill="var(--obsidian)"/>
      <path d="M0 40 H636 L640 36 L640 44 H0 Z" fill="var(--band-grey)"/>
    </svg>
  </section>

</main>
</body>
</html>
```